Aerial photo/video drone company needs new business card

Aerial visual company who offers photos and video services via drones.

We are KTO certified and work in the real estate, insurance, construction, and film industries.

I'm looking for a clean, professional, maybe even edgy design, that will be a conversation starter when networking.

I've included our logo, current business card, and font.

Our current business card is decent; albeit, I'm looking for something more unique. If you folks provide good designs, I'll definitely guarantee payment (and I'm not opposed to tipping if the design is above and beyond).

Target Market(s)

Insurance companies, real estate agents, construction companies, advertising & other creative agencies, and filmmakers/producers.

Industry/Entity Type

Business

Contact Information for Business Card

Company name pronounced tol-u-mo.

Other font styles liked:
• Font was uploaded; that or similar; not opposed to other fonts if they work well with the design

Requirements
Must have
• Clearly prominent logo; my name and title; phone number; email address; web address; mentioned "KTO Certified" or similar; should indicate "Aerial visual"
Nice to have
• Watermark of logo or otherwise
Should not have
• Pictures of drones or scenic shots

```html
<!DOCTYPE html>
<html lang="en">
<head>
<meta charset="utf-8">
<title>tolumo business card</title>
<link rel="stylesheet" href="https://fonts.googleapis.com/css2?family=Montserrat:wght@400;500;600;700&family=Open+Sans:wght@400;600&display=swap">
<style>
  :root{
    --page:#eceae6;
    --charcoal:#2c2e33;
    --navy:#2f4563;
    --navy-deep:#22344d;
    --sky:#5fb1e2;
    --blue:#2e8fd4;
    --slate:#7c8b9c;
    --white:#ffffff;
    --mist:#e6edf5;
    --mist-deep:#d5dde7;
  }
  *{box-sizing:border-box;margin:0;padding:0}
  html,body{width:1200px;height:800px;overflow:hidden}
  body{
    background:var(--page);
    font-family:"Montserrat",sans-serif;
    display:flex;align-items:center;justify-content:center;gap:40px;
  }
  .card{
    width:540px;height:309px;border-radius:18px;position:relative;overflow:hidden;
    box-shadow:0 10px 30px rgba(0,0,0,.15);
  }
  /* front */
  .card--front{background:var(--charcoal)}
  .front-mark{position:absolute;left:40px;top:60px;width:190px;height:190px;border-radius:50%;
    background:linear-gradient(135deg,var(--navy),var(--sky));}
  .front-brand{position:absolute;right:36px;top:78px;text-align:right}
  .wordmark{display:flex;align-items:center;gap:10px;font-weight:700;letter-spacing:1px;line-height:1}
  .front-brand .wordmark{justify-content:flex-end;font-size:54px;color:var(--sky)}
  .wordmark__dot{width:18px;height:18px;border-radius:50%;background:currentColor;flex:none}
  .tagline{margin-top:10px;font-size:13px;font-weight:600;color:var(--blue)}
  .industries{margin-top:16px;font-size:12px;font-weight:500;color:var(--white);letter-spacing:.3px;word-spacing:2px}
  /* back */
  .card--back{background:var(--white)}
  .back-watermark{position:absolute;left:-30px;top:120px;width:220px;height:220px;border-radius:50%;
    background:linear-gradient(135deg,var(--mist-deep),var(--mist));}
  .back-brand{position:absolute;left:40px;top:44px}
  .back-brand .wordmark{font-size:46px;color:var(--navy)}
  .contact-panel{position:absolute;right:0;top:40px;width:250px;height:140px;
    background:var(--blue);border-radius:12px 0 0 12px;padding:24px 22px;
    display:flex;flex-direction:column;justify-content:space-between}
  .contact{display:flex;align-items:center;gap:12px;font-family:"Open Sans",sans-serif;font-size:14px;color:var(--white)}
  .contact svg{width:16px;height:16px;flex:none}
  .name-band{position:absolute;left:0;bottom:32px;width:400px;height:74px;background:var(--navy-deep);
    padding:12px 40px;border-radius:0 12px 12px 0}
  .person{font-size:24px;font-weight:600;color:var(--white);line-height:1.2}
  .role{margin-top:4px;font-size:14px;color:var(--sky)}
</style>
</head>
<body>
  <section class="card card--front">
    <div class="front-mark" role="img" aria-label="Brand symbol area"></div>
    <div class="front-brand">
      <div class="wordmark"><span class="wordmark__dot"></span>tolumo</div>
      <div class="tagline">Aerial Visual for</div>
      <div class="industries">Real Estate | Insurance | Construction | Film</div>
    </div>
  </section>

  <section class="card card--back">
    <div class="back-watermark" role="img" aria-label="Faint brand symbol watermark"></div>
    <div class="back-brand">
      <div class="wordmark"><span class="wordmark__dot"></span>tolumo</div>
    </div>
    <div class="contact-panel">
      <div class="contact">
        <svg viewBox="0 0 16 16" fill="none" stroke="#fff" stroke-width="1.5"><rect x="1" y="3" width="14" height="10" rx="1"/><path d="M1 4l7 5 7-5"/></svg>
        dan@tolumo.com
      </div>
      <div class="contact">
        <svg viewBox="0 0 16 16" fill="#fff"><path d="M3 1h3l1 4-2 1a9 9 0 0 0 5 5l1-2 4 1v3c0 1-1 2-2 2A13 13 0 0 1 1 3c0-1 1-2 2-2z"/></svg>
        555.014.2287
      </div>
      <div class="contact">
        <svg viewBox="0 0 16 16" fill="none" stroke="#fff" stroke-width="1.3"><circle cx="8" cy="8" r="7"/><ellipse cx="8" cy="8" rx="3" ry="7"/><path d="M1 8h14M2.5 4.5h11M2.5 11.5h11"/></svg>
        tolumo.com
      </div>
    </div>
    <div class="name-band">
      <div class="person">Daniel P. Marsh</div>
      <div class="role">Owner | KTO Certified sUAS Pilot</div>
    </div>
  </section>
</body>
</html>
```